Homes, Invest in Non-performing loans

We need only 3 web pages, one for the home, one for the content, one for the properties.
The main focus of our business is to offer non performing loans (before foreclosures) to the general public. All the non-performing mortgages will end in a house, an apartment, a store, etc.
Our customers are able to invest from 10,000usd to 1,000,000usd (average 50,000usd).
Our customers' usual focus groups are employees who want second earnings, perceiving the business feeling without outlay time. They look for a solid finance sense corporation that confers them certainty.
Nearly all our clients desire the house, apartment, store, etc. more than the actual earnings.
The name of our company is BRAMLEX
Reason: We value the time and effort you already invest in our project. We realize that we did't come back on some of the doubts requested by the designers. It will be inequitable to the designers who prerequisite our feedback. We also appreciate the comprehension of the community in this postponement.
Reason: Designers,
We really apreciate all the time and effort you put on our project. From the begining we ask for 3 pages, so now we will leave the 10 finalist and provide some extra time to submit the other 2 pages.
We will race the price in 10%
Target Market(s)
Our customers average investors works as employees and want to have a second income or business without spending time. (People from 35 to 50)
Industry/Entity Type
Finance
Requirements
Should not have
- FLASH

```html
<!DOCTYPE html>
<html lang="es">
<head>
<meta charset="utf-8">
<title>BRAMLEX · Remates Hipotecarios</title>
<link rel="stylesheet" href="https://fonts.googleapis.com/css2?family=Oswald:wght@300;400;600;700&display=swap">
<style>
:root{
  --olive:#a8a204;
  --olive-text:#b0aa1f;
  --olive-light:#efec9c;
  --caption-olive:#cdc86a;
  --ink:#2e2e2e;
  --body-text:#3a3a3a;
  --white:#ffffff;
  --tab-grey:#d9d9d9;
  --hero-a:#a39b92;
  --hero-b:#847d74;
}
*{margin:0;padding:0;box-sizing:border-box}
html,body{width:1200px;height:1060px;overflow:hidden}
body{
  position:relative;
  font-family:"Oswald",sans-serif;
  font-weight:300;
  color:var(--body-text);
  background:linear-gradient(180deg,#ececec 0,#f4f4f4 60%,#ffffff 100%);
}
.top-rule{position:absolute;left:0;top:0;width:1200px;height:6px;background:var(--olive)}
.brand-panel{position:absolute;left:100px;top:6px;width:211px;height:250px;z-index:3}
.brand-panel svg{position:absolute;inset:0}
.brand-name{position:absolute;left:0;top:70px;width:211px;text-align:center;font-weight:700;font-size:46px;letter-spacing:1px;color:var(--ink);line-height:1}
.brand-mark{position:absolute;left:90px;top:24px;width:30px;height:30px;background:var(--olive)}
.brand-tag{position:absolute;left:23px;top:158px;width:162px;border-top:1px solid #bbb;padding-top:5px;font-size:10.5px;font-weight:400;letter-spacing:2.1px;color:var(--ink);text-align:center}
.contact{position:absolute;top:15px;font-size:16px;color:var(--olive-text);display:flex;align-items:center;gap:8px;letter-spacing:-.3px}
.contact.mail{left:731px}
.contact.phone{left:917px}
.main-nav{position:absolute;left:586px;top:112px;width:514px;height:33px}
.main-nav svg{position:absolute;inset:0}
.main-nav ul{position:absolute;left:0;top:0;height:33px;list-style:none}
.main-nav li{position:absolute;color:var(--white);font-size:14.5px;font-weight:400;white-space:nowrap;top:7px;letter-spacing:-.2px}
.slider{position:absolute;left:100px;top:145px;width:1000px;height:433px;overflow:hidden;
  box-shadow:0 10px 12px -8px rgba(0,0,0,.35)}
.slider-photo{position:absolute;inset:0;background:linear-gradient(180deg,var(--hero-a),var(--hero-b))}
.slider-caption{position:absolute;left:0;bottom:0;width:1000px;height:70px;background:linear-gradient(180deg,#3b3b3b,#242424)}
.caption-kicker{position:absolute;left:22px;top:11px;color:var(--white);font-size:15px;font-weight:400;letter-spacing:-.2px}
.caption-line{position:absolute;left:22px;top:31px;font-size:19px;color:var(--caption-olive);letter-spacing:-.2px}
.slider-dots{position:absolute;left:842px;top:0;width:141px;height:23px}
.arrow{position:absolute;top:305px;width:30px;height:80px;z-index:2}
.arrow.prev{left:100px}.arrow.next{left:1070px}
.card{position:absolute;top:604px;width:326px;height:349px;border-radius:4px 4px 0 0;overflow:hidden;
  background:linear-gradient(180deg,#d8d8d8 0,#e6e6e6 55%,#fafafa 100%)}
.card h2{height:52px;background:linear-gradient(180deg,#aea707,#9f9900);color:var(--olive-light);font-weight:400;font-size:17.5px;text-align:center;line-height:52px;letter-spacing:-.4px}
.card p{margin:22px 25px 0;font-size:15.2px;line-height:20.7px;text-align:justify;color:var(--body-text);letter-spacing:-.25px}
.card p + p{margin-top:0}
.card sup{font-size:8px;line-height:0;vertical-align:6px}
.card.one{left:100px}.card.two{left:437px}.card.three{left:774px}
.follow-tab{position:absolute;left:903px;top:954px;width:134px;height:30px;background:var(--tab-grey);border-radius:4px 4px 0 0;text-align:center;font-size:12px;font-weight:400;color:var(--ink);line-height:34px;letter-spacing:-.2px}
.site-footer{position:absolute;left:100px;top:984px;width:1000px;height:76px;background:var(--olive);border-radius:4px 4px 0 0}
.footer-nav{list-style:none}
.footer-nav li{position:absolute;top:23px;color:var(--white);font-size:14.5px;font-weight:400;letter-spacing:-.2px}
.social{position:absolute;left:791px;top:6px}
</style>
</head>
<body>
<div class="top-rule"></div>

<div class="brand-panel">
  <svg width="211" height="250" viewBox="0 0 211 250"><polygon points="0,0 211,0 211,185 105,250 0,185" fill="#ffffff"/></svg>
  <div class="brand-mark"></div>
  <div class="brand-name">BRAMLEX</div>
  <div class="brand-tag">REMATES HIPOTECARIOS</div>
</div>

<div class="contact mail">
  <svg width="20" height="14" viewBox="0 0 20 14"><rect x=".75" y=".75" width="18.5" height="12.5" fill="none" stroke="#555" stroke-width="1.5"/><polyline points="1,1 10,8 19,1" fill="none" stroke="#555" stroke-width="1.5"/><line x1="1" y1="13" x2="7.5" y2="6.5" stroke="#555" stroke-width="1.2"/><line x1="19" y1="13" x2="12.5" y2="6.5" stroke="#555" stroke-width="1.2"/></svg>
  <span>ventas@bramlex.mx</span>
</div>
<div class="contact phone">
  <svg width="14" height="16" viewBox="0 0 14 16"><path d="M3 1l3 3-1.5 2c1 2 2.5 3.5 4.5 4.5L11 9l3 3-2 3C6 14 1 9 0 3z" fill="#666"/></svg>
  <span>VENTAS (55) 4810 - 3370</span>
</div>

<nav class="main-nav">
  <svg width="514" height="33" viewBox="0 0 514 33"><path d="M14,0 H508 Q514,0 514,6 V33 H0 Z" fill="#a8a204"/></svg>
  <ul>
    <li style="left:42px">Remates</li>
    <li style="left:136px">Quienes Somos</li>
    <li style="left:268px">Contacto</li>
    <li style="left:365px">Acceso</li>
    <li style="left:451px">Inicio</li>
  </ul>
</nav>

<section class="slider">
  <div class="slider-photo" role="img" aria-label="Fotografía de una gran casa residencial con jardín"></div>
  <div class="slider-caption">
    <svg class="slider-dots" width="141" height="23" viewBox="0 0 141 23">
      <path d="M0,0 H141 L134,23 H7 Z" fill="#6a6a6a"/>
      <circle cx="40" cy="12" r="5" fill="#2a2a2a"/>
      <circle cx="57" cy="12" r="5" fill="#b5ae15"/>
      <circle cx="75" cy="12" r="5" fill="#b5ae15"/>
      <circle cx="92" cy="12" r="5" fill="#b5ae15"/>
      <circle cx="109" cy="12" r="5" fill="#b5ae15"/>
    </svg>
    <div class="caption-kicker">ES UNA INVERSIÓN Y UNA CASA</div>
    <div class="caption-line">Comprar un Remate Hipotecario en BRAMLEX®, es una excelente forma de inversión</div>
  </div>
</section>
<svg class="arrow prev" viewBox="0 0 30 80"><path d="M0,0 A40,40 0 0 1 0,80 Z" fill="#9a9a9a" opacity=".85"/><polygon points="13,32 4,40 13,48" fill="#fff"/></svg>
<svg class="arrow next" viewBox="0 0 30 80"><path d="M30,0 A40,40 0 0 0 30,80 Z" fill="#9a9a9a" opacity=".85"/><polygon points="17,32 26,40 17,48" fill="#fff"/></svg>

<article class="card one">
  <h2>REMATES HIPOTECARIOS</h2>
  <p>Al contratar con nosotros tu obtienes una Cesión de Derechos con la garantía de la propiedad que elijas, cuya ejecución la lleva a cabo BRAMLEX<sup>®</sup> a través del remate judicial.</p>
  <p>En BRAMLEX<sup>®</sup> contamos con una amplia gama de Cesiones de Derechos que puedes adquirir, mismos que se encuentran en distintas etapas judiciales. Las oportunidades con las que contamos permiten adquirir una propiedad por menos de su valor real.</p>
</article>
<article class="card two">
  <h2>NOSOTROS</h2>
  <p>Al contratar con nosotros tu obtienes una Cesión de Derechos con la garantía de la propiedad que elijas, cuya ejecución la lleva a cabo BRAMLEX<sup>®</sup> a través del remate judicial.</p>
  <p>En BRAMLEX<sup>®</sup> contamos con una amplia gama de Cesiones de Derechos que puedes adquirir, mismos que se encuentran en distintas etapas judiciales. Las oportunidades con las que contamos permiten adquirir una propiedad por menos de su valor real.</p>
</article>
<article class="card three">
  <h2>SERVICIOS</h2>
  <p>Al contratar con nosotros tu obtienes una Cesión de Derechos con la garantía de la propiedad que elijas, cuya ejecución la lleva a cabo BRAMLEX<sup>®</sup> a través del remate judicial.</p>
  <p>En BRAMLEX<sup>®</sup> contamos con una amplia gama de Cesiones de Derechos que puedes adquirir, mismos que se encuentran en distintas etapas judiciales. Las oportunidades con las que contamos permiten adquirir una propiedad por menos de su valor real.</p>
</article>

<div class="follow-tab">FOLLOW US ON :</div>
<footer class="site-footer">
  <ul class="footer-nav">
    <li style="left:17px">Remates</li>
    <li style="left:111px">Quienes Somos</li>
    <li style="left:243px">Contacto</li>
    <li style="left:340px">Acceso</li>
    <li style="left:427px">Inicio</li>
  </ul>
  <svg class="social" width="180" height="40" viewBox="0 0 180 40" role="img" aria-label="Enlaces a redes sociales">
    <g fill="none" stroke="#ffffff" stroke-width="3">
      <circle cx="20" cy="19" r="16"/><circle cx="65" cy="19" r="16"/>
      <circle cx="111" cy="19" r="16"/><circle cx="157" cy="19" r="16"/>
    </g>
  </svg>
</footer>
</body>
</html>
```